Custom Die cut yard sign

Hi!

I would love to get really eye catching creative here with some window cleaning die cut signs!

I would like the main words to stand out of just saying, "Window Cleaning"

My phone number: 612-555-0148
Website: BrightpaneMN.com

My logo but it can be small as I want the "Window Cleaning and Phone number to really pop.

It can be a creative for implying window cleaning! Die cut so maybe water? Light? Windows outlines, squeegee? I don't know it's for residential window cleaning!

Attached is my logo and the template for the die cut sign.

Thanks!

```html
<!DOCTYPE html>
<html lang="en">
<head>
<meta charset="UTF-8">
<title>Brightpane Window Cleaning – Yard Sign</title>
<link href="https://fonts.googleapis.com/css2?family=Bebas+Neue&family=Montserrat:wght@800&display=swap" rel="stylesheet">
<style>
  :root {
    --backdrop: #c8c8c8;
    --navy: #003d6b;
    --navy-deep: #00345c;
    --sky-glow: #0a90d2;
    --lime: #bcd630;
    --leaf: #7cc142;
    --white: #ffffff;
  }
  * { margin: 0; padding: 0; box-sizing: border-box; }
  html, body {
    width: 767px;
    height: 1200px;
    overflow: hidden;
    background: var(--backdrop);
  }
  .yard-sign {
    position: absolute;
    left: 44px;
    top: 344px;
    width: 680px;
    height: 512px;
    background: var(--white);
    box-shadow: 0 2px 6px rgba(0,0,0,0.25);
    overflow: hidden;
  }
  .headline-band {
    position: absolute;
    left: 0; top: 0;
    width: 100%;
    height: 328px;
    background: radial-gradient(ellipse 48% 62% at 50% 47%, var(--sky-glow) 0%, #0068a6 45%, var(--navy) 80%, var(--navy-deep) 100%);
    text-align: center;
  }
  .headline-word {
    display: block;
    font-family: 'Bebas Neue', sans-serif;
    line-height: 1;
  }
  .headline-word--window {
    position: absolute;
    left: 0; right: 0;
    top: 20px;
    font-size: 160px;
    color: var(--white);
    letter-spacing: 1px;
  }
  .headline-word--cleaning {
    position: absolute;
    left: 0; right: 0;
    top: 136px;
    font-size: 202px;
    letter-spacing: 2px;
    background: linear-gradient(180deg, var(--lime) 20%, var(--leaf) 85%);
    -webkit-background-clip: text;
    background-clip: text;
    color: transparent;
  }
  .accent-stripe {
    position: absolute;
    left: 0; top: 328px;
    width: 100%;
    height: 7px;
    background: var(--lime);
  }
  .contact-panel {
    position: absolute;
    left: 0; top: 335px;
    width: 100%;
    height: 177px;
  }
  .brand-mark {
    position: absolute;
    left: 36px;
    top: 44px;
    width: 200px;
    display: flex;
    align-items: center;
    gap: 8px;
  }
  .brand-dot {
    width: 34px;
    height: 34px;
    border-radius: 50%;
    background: var(--navy);
    flex: none;
  }
  .brand-name {
    font-family: 'Bebas Neue', sans-serif;
    font-size: 30px;
    line-height: 0.95;
    color: var(--navy);
  }
  .phone-number {
    position: absolute;
    left: 266px;
    top: 26px;
    font-family: 'Bebas Neue', sans-serif;
    font-size: 86px;
    line-height: 1;
    color: var(--navy);
    letter-spacing: 0.5px;
  }
  .web-address {
    position: absolute;
    left: 268px;
    top: 110px;
    font-family: 'Montserrat', sans-serif;
    font-weight: 800;
    font-size: 23px;
    color: var(--navy);
    letter-spacing: 1px;
  }
</style>
</head>
<body>
  <main class="yard-sign">
    <section class="headline-band">
      <span class="headline-word headline-word--window">WINDOW</span>
      <span class="headline-word headline-word--cleaning">CLEANING</span>
    </section>
    <div class="accent-stripe"></div>
    <section class="contact-panel">
      <div class="brand-mark">
        <span class="brand-dot"></span>
        <span class="brand-name">BRIGHTPANE<br>WINDOW CLEANING</span>
      </div>
      <div class="phone-number">612-555-0148</div>
      <div class="web-address">www.BrightpaneMN.com</div>
    </section>
  </main>
</body>
</html>
```